Elegant Financial Planning Business Card

Clearpath Wealth Advisory Pty Ltd requires an elegant business card that communicates simplicity, elegance and trust.
Attached card example of 'Varnoth' is very close to what I am looking for. Looking for black and white card.
Update 24/1/16: The attached Varnoth card is almost exactly what I am looking for. Although it is possible that alternative layouts may interest me, it is considerably more likely that I will proceed with a virtual clone of the "Varnoth' example.
Industry/Entity Type
Financial Planning
Contact Information for Business Card
In black font...
Front Details are (layout as per Dana Varnoth card picture):
Line1 - Name: Oliver Marsh
Line 2 - Company: Clearpath Wealth Advisory Pty Ltd
Line 3 - Address: Harbourview Plaza 3, Level 17, 58 Lomond Avenue, Ardenmere Junction NRW
Line 4
- Phone: 136 712
- Email: advice@cpwa-example.com.au
- Site: www.cpwa-example.com.au
Back details
1/ logo in position and dimensions as per attached layout
2. Bottom left (in smaller writing).
- Authorised Representative No. 517946
- Clearpath Wealth Advisory is a corporate authorised representative of Tarquay7 Capital Services Pty Ltd
- ABN 47 318 602 154
- AFSL No. 608139

```html
<!DOCTYPE html>
<html lang="en">
<head>
<meta charset="utf-8">
<title>Clearpath Wealth Advisory – Business Card</title>
<link rel="stylesheet" href="https://fonts.googleapis.com/css2?family=Libre+Baskerville:wght@400;700&display=swap">
<style>
  :root {
    --stage: #e9e7e3;
    --paper: #ffffff;
    --ink: #111111;
    --card-black: #0b0b0b;
    --reverse-ink: #f4f4f4;
    --shadow: rgba(0, 0, 0, 0.18);
  }
  * { box-sizing: border-box; margin: 0; padding: 0; }
  html, body {
    width: 1200px;
    height: 700px;
    overflow: hidden;
    background: var(--stage);
    font-family: "Libre Baskerville", Georgia, serif;
  }
  .stage {
    position: relative;
    width: 1200px;
    height: 700px;
    display: flex;
    align-items: center;
    justify-content: center;
    gap: 50px;
  }
  .card {
    position: relative;
    width: 525px;
    height: 300px;
    box-shadow: 0 6px 18px var(--shadow);
  }
  .card--front { background: var(--paper); color: var(--ink); }
  .card--back { background: var(--card-black); color: var(--reverse-ink); }

  .wordmark {
    position: absolute;
    top: 34px;
    right: 34px;
    font-weight: 400;
    font-size: 38px;
    letter-spacing: 0.5px;
    line-height: 1;
  }
  .card--front .wordmark { color: var(--ink); }
  .card--back .wordmark { color: var(--reverse-ink); }

  .front-details {
    position: absolute;
    left: 34px;
    top: 128px;
  }
  .holder-name {
    font-weight: 700;
    font-size: 21px;
    letter-spacing: 0.3px;
  }
  .company {
    font-size: 8.5px;
    margin-top: 6px;
  }
  .address {
    font-size: 8.5px;
    margin-top: 14px;
  }
  .contact-list {
    list-style: none;
    margin-top: 26px;
    font-size: 8.5px;
  }
  .contact-list li {
    display: flex;
    align-items: center;
    gap: 6px;
    margin-bottom: 4px;
  }
  .contact-icon { width: 10px; height: 10px; flex: none; }
  .website {
    font-size: 8.5px;
    margin-top: 14px;
  }

  .back-legal {
    position: absolute;
    left: 34px;
    bottom: 74px;
    width: 270px;
  }
  .rep-number {
    font-size: 12px;
    letter-spacing: 0.3px;
  }
  .rep-statement {
    font-size: 7px;
    line-height: 1.5;
    margin-top: 6px;
  }
  .back-registration {
    position: absolute;
    right: 96px;
    bottom: 82px;
    text-align: right;
    font-size: 7px;
    line-height: 1.6;
  }
</style>
</head>
<body>
<main class="stage">
  <section class="card card--front" aria-label="Business card front">
    <div class="wordmark">Clearpath</div>
    <div class="front-details">
      <h1 class="holder-name">Oliver Marsh</h1>
      <p class="company">Clearpath Wealth Advisory Pty Ltd</p>
      <p class="address">Harbourview Plaza 3, Level 17, 58 Lomond Avenue, Ardenmere Junction NRW</p>
      <ul class="contact-list">
        <li>
          <svg class="contact-icon" viewBox="0 0 10 10" aria-hidden="true">
            <circle cx="5" cy="5" r="5" fill="#111"/>
            <path d="M3.3 2.6c.3-.2.6 0 .7.3l.3.7c.1.2 0 .4-.1.5l-.3.3c.3.6.8 1.1 1.4 1.4l.3-.3c.1-.1.3-.2.5-.1l.7.3c.3.1.4.4.3.7l-.2.4c-.2.3-.5.5-.9.4C4.5 6.8 3.2 5.5 2.8 4c-.1-.4.1-.7.4-.9z" fill="#fff"/>
          </svg>
          <span>136 712</span>
        </li>
        <li>
          <svg class="contact-icon" viewBox="0 0 10 10" aria-hidden="true">
            <circle cx="5" cy="5" r="5" fill="#111"/>
            <rect x="2.4" y="3.2" width="5.2" height="3.6" fill="none" stroke="#fff" stroke-width="0.7"/>
            <path d="M2.5 3.3 5 5.2 7.5 3.3" fill="none" stroke="#fff" stroke-width="0.7"/>
          </svg>
          <span>advice@cpwa-example.com.au</span>
        </li>
      </ul>
      <p class="website">www.cpwa-example.com.au</p>
    </div>
  </section>

  <section class="card card--back" aria-label="Business card back">
    <div class="wordmark">Clearpath</div>
    <div class="back-legal">
      <p class="rep-number">Authorised Representative No. 517946</p>
      <p class="rep-statement">Clearpath Wealth Advisory is a corporate authorised representative of Tarquay7 Capital Services Pty Ltd</p>
    </div>
    <div class="back-registration">
      <p>AFSL No. 608139</p>
      <p>ABN 47 318 602 154</p>
    </div>
  </section>
</main>
</body>
</html>
```